Vemtra Group: Business Card for a high end technology company

We need a cool new design for our business cards using our cloud logo. We are a technology consulting business. We pride ourselves on be the best of the best. We mainly focus on cloud solutions and managed services. We need a business card that sets us apart from the other technology companies in the area and allows us to stand out.

Target Market(s)

Technology departments, CIO, CEOs, and Information Technology Staff.

Industry/Entity Type

Information Technology

Contact Information for Business Card

Must have the logo and our name.
Must have employee name, email address, office phone, cell phone and website.
Need to have all info on one side a cool design on backside.

Font styles to use
Serif
Sans Serif

Requirements
Must have
• Must have the logo and our name.
• Must have employee name, email address, office phone, cell phone and website.
• Need to have all info on one side a cool design on back side.
• Must be a crisp clean design, not too busy or confusing.

```html
<!DOCTYPE html>
<html lang="en">
<head>
<meta charset="utf-8">
<title>Vemtra Group — Stationery</title>
<link href="https://fonts.googleapis.com/css2?family=Open+Sans:wght@400;600;700&family=Raleway:wght@400&display=swap" rel="stylesheet">
<style>
  :root{
    --stage:#363636;
    --paper:#ffffff;
    --ink:#2b2b2b;
    --ink-soft:#4a4a4a;
    --blue:#2f9fe0;
    --blue-deep:#2a6fc4;
    --blue-light:#8fd4f1;
    --sky-pale:#e9f6fc;
  }
  *{margin:0;padding:0;box-sizing:border-box}
  html,body{width:1200px;height:1050px;overflow:hidden}
  body{background:var(--stage);position:relative;font-family:"Open Sans",Arial,sans-serif;color:var(--ink)}
  .sheet{position:absolute;background:var(--paper);overflow:hidden;box-shadow:0 6px 14px rgba(0,0,0,.35)}

  /* brand lockup */
  .brand{position:absolute;display:flex;flex-direction:column;align-items:center}
  .brand-dot{border-radius:50%;background:var(--blue)}
  .brand-name{font-family:"Raleway","Open Sans",sans-serif;font-weight:400;color:var(--ink);white-space:nowrap;line-height:1}
  .brand-url{font-weight:600;color:var(--ink);white-space:nowrap;line-height:1}

  .ribbon{position:absolute;background:radial-gradient(ellipse at 70% 60%, var(--blue) 0%, var(--blue-deep) 38%, rgba(47,159,224,.35) 62%, rgba(255,255,255,0) 75%)}

  /* letterhead */
  .letterhead{left:186px;top:185px;width:383px;height:495px}
  .letter-body{position:absolute;left:30px;top:125px;width:315px;font-size:6.3px;line-height:7.9px;color:var(--ink-soft);text-align:justify}
  .letter-body p{margin-bottom:8px}
  .signoff{position:absolute;left:30px;top:351px;font-size:6.3px;line-height:8px;color:var(--ink-soft)}
  .signoff strong{color:var(--ink)}

  /* cover */
  .cover{left:600px;top:140px;width:405px;height:540px;background:radial-gradient(ellipse at 20% 95%, #f3fafd 0%, #bfe6f7 45%, var(--blue-light) 100%)}

  /* business cards */
  .card-front{left:75px;top:715px;width:157px;height:90px}
  .card-divider{position:absolute;left:86px;top:18px;width:1px;height:54px;background:#c9c9c9}
  .card-info{position:absolute;left:97px;top:22px;font-size:3.6px;line-height:4.7px;color:var(--ink-soft)}
  .card-info .person{color:var(--blue);font-weight:700;font-size:4.4px}
  .card-info .role{margin-bottom:4px}
  .card-info .gap{height:3px}
  .card-back{left:75px;top:831px;width:157px;height:90px;background:linear-gradient(135deg,#fff 30%,var(--sky-pale) 100%)}
  .card-back .site{position:absolute;left:8px;bottom:6px;font-size:3.4px;color:var(--ink-soft)}

  /* envelope */
  .envelope{left:253px;top:715px;width:427px;height:192px;background:radial-gradient(ellipse at 50% 35%, #fff 0%, #f1f1f1 100%)}
  .sender{position:absolute;left:18px;top:146px;font-size:5.8px;line-height:8px;color:var(--ink-soft)}
  .sender strong{color:var(--ink)}

  /* compliment slip */
  .slip{left:709px;top:715px;width:427px;height:192px}
  .slip-contact{position:absolute;left:22px;top:133px;font-size:5.8px;line-height:8.2px;color:var(--ink-soft)}
</style>
</head>
<body>

<section class="sheet letterhead">
  <div class="brand" style="left:262px;top:27px">
    <span class="brand-dot" style="width:22px;height:22px;margin-bottom:6px"></span>
    <span class="brand-name" style="font-size:14px">Vemtra Group</span>
    <span class="brand-url" style="font-size:4.5px;margin-top:3px">www.vemtragroup.com</span>
  </div>
  <div class="letter-body">
    <p>Lorem ipsum dolor sit amet, consectetur adipiscing elit. Vivamus sed vulputate risus. Aenean ut vulputate orci. Aliquam sit amet venenatis nisl. Aliquam enim velit, sagittis vel dolor hendrerit, eleifend sagittis velit. Nam dolor ex, consequat sed scelerisque at, porttitor et sapien. Sed libero quam, pretium vitae sem a, egestas malesuada tellus. Donec nibh nibh, mattis ac posuere quis, viverra id libero. Etiam dapibus fermentum tortor. Nullam suscipit lacinia aliquet. Morbi euismod dolor ac ex pharetra, sit amet congue erat tincidunt. Suspendisse felis sapien, maximus eget laoreet vel, consequat eget libero. Sed nec fringilla dui. Proin laoreet lacus nec eros ultricies fringilla. Vestibulum vel condimentum diam. Pellentesque purus erat, blandit nec velit eget, dictum porta ex. Nulla facilisi. Donec sed odio tincidunt, ultrices justo vitae, porttitor urna. Class aptent taciti sociosqu ad litora torquent per conubia nostra, per inceptos himenaeos. Vestibulum justo ju</p>
    <p>sto, facilisis id urna vitae, eleifend vehicula urna. Ut luctus nisi quis tortor sollicitudin pellentesque. Aenean urna tortor, molestie vitae ante eget, sodales blandit quam. Quisque eget nunc scelerisque ligula ultrices tristique. Pellentesque habitant morbi tristique senectus et netus et malesuada fames ac turpis egestas. Suspendisse potenti. Donec ultricies, diam ut mollis sodales, leo quam sollicitudin ipsum, sed dignissim erat odio non lectus. Praesent tincidunt elit sit amet dolor tempus, ut pellentesque diam aliquam. Duis maximus lacinia metus sed ultrices. Mauris ut urna efficitur orci ultrices viverra. Vestibulum luctus orci in lectus suscipit, a aliquam ex cursus. Praesent metus mi, ultricies sit amet rutrum id, hendrerit ut diam.</p>
    <p>Nunc iaculis, arcu eu facilisis sodales, turpis sem placerat libero, sed venenatis risus sem sed est. Maecenas tristique, eros et dignissim convallis, nunc diam interdum nulla, et gravida erat turpis quis risus. Nunc ut velit vitae felis pulvinar pellentesque. Aenean vitae turpis a ligula tempus lobortis eu in ante. Nunc sed lacus id odio commodo auctor. Donec interdum maximus augue non fringilla. Mauris cursus sapien quis massa ultrices, non convallis ex auctor.</p>
  </div>
  <div class="signoff">Your Sincerely<br><strong>Name Surname</strong></div>
  <div class="ribbon" role="img" aria-label="Large blue ribbon decoration in the corner" style="left:140px;top:335px;width:260px;height:180px"></div>
</section>

<section class="sheet cover">
  <div class="brand" style="left:42px;top:432px">
    <span class="brand-dot" style="width:24px;height:24px;margin-bottom:7px"></span>
    <span class="brand-name" style="font-size:14.5px">Vemtra Group</span>
    <span class="brand-url" style="font-size:4.6px;margin-top:3px">www.vemtragroup.com</span>
  </div>
</section>

<section class="sheet card-front">
  <div class="brand" style="left:22px;top:25px">
    <span class="brand-dot" style="width:15px;height:15px;margin-bottom:5px"></span>
    <span class="brand-name" style="font-size:9px">Vemtra Group</span>
    <span class="brand-url" style="font-size:3px;margin-top:2px">www.vemtragroup.com</span>
  </div>
  <div class="card-divider"></div>
  <div class="card-info">
    <div class="person">Daniel Marlowe</div>
    <div class="role">Creative Director</div>
    <div>d.marlowe@email.com</div>
    <div>P: +01 555 210 4410</div>
    <div>M: +01 555 210 4411</div>
    <div class="gap"></div>
    <div>www.vemtragroup.com</div>
    <div>Harbour City, Australia</div>
    <div>PO Box 480</div>
  </div>
</section>

<section class="sheet card-back">
  <div class="brand" style="left:8px;top:12px">
    <span class="brand-dot" style="width:10px;height:10px;margin-bottom:3px"></span>
    <span class="brand-name" style="font-size:6px">Vemtra Group</span>
  </div>
  <div class="ribbon" role="img" aria-label="Blue ribbon decoration" style="left:55px;top:35px;width:115px;height:70px"></div>
  <div class="site">www.vemtragroup.com</div>
</section>

<section class="sheet envelope">
  <div class="sender"><strong>VEMTRA GROUP</strong><br>Technology Consulting<br>Cloud Solutions &amp; Managed Services</div>
  <div class="brand" style="left:335px;top:128px">
    <span class="brand-dot" style="width:18px;height:18px;margin-bottom:5px"></span>
    <span class="brand-name" style="font-size:11px">Vemtra Group</span>
    <span class="brand-url" style="font-size:3.6px;margin-top:2px">www.vemtragroup.com</span>
  </div>
</section>

<section class="sheet slip">
  <div class="brand" style="left:22px;top:22px">
    <span class="brand-dot" style="width:18px;height:18px;margin-bottom:5px"></span>
    <span class="brand-name" style="font-size:11px">Vemtra Group</span>
    <span class="brand-url" style="font-size:3.6px;margin-top:2px">www.vemtragroup.com</span>
  </div>
  <div class="slip-contact">
    lena.hart@mail.com<br>
    www.northfieldco.com<br>
    +01 555 210 4410<br>
    +01 555 210 4410<br>
    7th floor, P.O.Box 480, Harbour City, Australia
  </div>
  <div class="ribbon" role="img" aria-label="Large blue ribbon decoration" style="left:215px;top:60px;width:240px;height:150px"></div>
</section>

</body>
</html>
```